WILLOW DENTAL BLOG - Tooth Whitening Edition

Blog Design for Willow Dental Practice. Willow Dental is a dental practice that places emphasis on patient care. We provide high quality care and offer a wide variety of treatments.
Dental Implants, Crowns and Veneers and R lume Orthodontics are some of our Services
First Blog should Introduce us and our Services. We intend to link our blog to website- our website is to be redone but at the moment it is www.willowdental-example.com.au
we should avoid putting pricing or promotions on the blog. focus on patient education and cosmetics
First Blog topic should centre on info and pt education around tooth whitening
some before and after photos of our patients are attached
link us on Chatterly
we are rated 5 stars on zorvo review and teal ledger and it will be good if blog reflects this

Target Market(s)

Patients interested in Cosmetic/Aesthetic Dentistry

Industry/Entity Type

Dental

Font styles to use
Sans Serif
Decorative
Script

Requirements
Must have
• Willow Dental Logo.
• Willow Dental address and details
• Info and write up on tooth whitening
Nice to have
• Creative and attractive Blog that can be added to and built up overtime, i.e I can write future blog to this site
• link to website willowdental-example.com.au
• showcase our high review ratings
• social media boost
• will be good if we can redraw/reanimate/design the pictures i have included in the blog write up- because they were copied from zorvo images- no copywrite
Should not have
• pricing or promotions

```html
<!DOCTYPE html>
<html lang="en">
<head>
<meta charset="utf-8">
<title>Willow Dental Blog – Tooth Whitening</title>
<link href="https://fonts.googleapis.com/css2?family=Open+Sans:wght@400;600;700&display=swap" rel="stylesheet">
<style>
:root{
  --blue:#3a78b5;
  --blue-dark:#2c5f93;
  --blue-text:#2f6fae;
  --ink:#4a4a4a;
  --muted:#6f6f6f;
  --line:#dcdcdc;
  --panel:#f2f2f2;
  --white:#fff;
  --star:#f2a100;
}
*{box-sizing:border-box;margin:0;padding:0}
html,body{width:1200px;height:2824px;overflow:hidden;background:var(--white)}
body{font-family:"Open Sans",Arial,sans-serif;color:var(--ink);font-size:14px;line-height:1.5}
.page{position:relative;width:1200px;height:2824px}
.photo{display:block}
a{color:var(--blue-text);text-decoration:none}

/* hero */
.hero{position:absolute;left:0;top:0;width:1200px;height:580px;
  background:linear-gradient(100deg,#5d8fbf 0%,#8fb6d9 35%,#e9d3c2 60%,#f4e3cf 80%,#a8c6df 100%)}
.brand{position:absolute;left:40px;top:18px;display:flex;align-items:center;gap:10px}
.brand-mark{width:40px;height:40px;border-radius:50%;background:var(--white)}
.brand-name{font-weight:700;font-size:20px;color:var(--white);line-height:1.1}
.brand-tag{font-size:12px;color:var(--white)}
.main-nav{position:absolute;right:40px;top:30px;display:flex;gap:6px}
.main-nav a{color:var(--white);font-size:14px;font-weight:600;padding:8px 14px}
.main-nav a.active{background:var(--blue)}
.hero-title{position:absolute;left:40px;top:220px;font-size:58px;font-weight:700;color:var(--white);line-height:1.2}
.hero-lead{position:absolute;left:40px;top:300px;width:580px;font-size:27px;font-weight:700;line-height:1.3;color:var(--white)}
.btn{display:inline-block;background:var(--blue);color:var(--white);font-weight:600;font-size:14px;padding:8px 20px;border-radius:3px}
.hero .btn{position:absolute;left:40px;top:440px;font-size:18px;padding:10px 30px}

/* intro band */
.intro{position:absolute;left:0;top:592px;width:1200px;height:228px;background:var(--blue);color:var(--white)}
.intro h2{position:absolute;left:40px;top:22px;font-size:26px;font-weight:600}
.intro p{position:absolute;left:40px;top:70px;width:540px;font-size:13px;line-height:1.6}
.intro .photo{position:absolute;left:620px;top:22px;width:540px;height:184px;background:linear-gradient(90deg,#c98b86,#f4f1ec 45%,#f8f8f6 55%,#c67d78)}

/* services */
.services{position:absolute;left:0;top:840px;width:1200px;height:370px;display:flex;justify-content:space-around;padding:0 40px}
.service{width:240px;text-align:center}
.service .photo{width:180px;height:180px;border-radius:50%;margin:20px auto 14px;border:4px solid var(--line)}
.service h3{color:var(--blue-text);font-size:17px;font-weight:600}
.service p{font-size:12px;color:var(--muted);margin:6px 0 12px}
.service .btn{font-size:12px;padding:5px 14px}

/* articles */
.articles{position:absolute;left:0;top:1220px;width:1200px;height:390px;background:var(--panel);border-top:2px solid var(--line);display:grid;grid-template-columns:1fr 1fr;gap:30px 50px;padding:30px 40px}
.article{display:flex;gap:20px}
.article .photo{flex:0 0 160px;height:120px;background:linear-gradient(135deg,#e8c1a8,#f6e8dc 50%,#b9786e)}
.article h3{color:var(--blue-text);font-size:17px;font-weight:600}
.article .date{font-size:12px;color:var(--muted)}
.article p{font-size:12px;color:var(--muted);margin-top:4px}

/* testimonials */
.testimonials{position:absolute;left:0;top:1640px;width:1200px;height:380px;padding:0 40px}
.section-title{color:var(--blue-text);font-size:26px;font-weight:600}
.quotes{position:absolute;left:40px;top:50px;width:370px}
.quote{border:1px solid var(--line);padding:14px;font-size:12px;color:var(--muted);margin-bottom:10px;border-radius:3px}
.quote-author{font-size:12px;display:block;margin:-4px 0 12px}
.smile-grid{position:absolute;left:440px;top:20px;display:grid;grid-template-columns:repeat(4,170px);gap:14px}
.smile-grid .photo{height:150px;background:linear-gradient(135deg,#c99478,#efd9c8 50%,#a26c58)}

/* reviews */
.reviews{position:absolute;left:0;top:2040px;width:1200px;height:340px;padding:0 40px}
.reviews .section-title{font-size:22px}
.review-list{position:absolute;left:40px;top:50px;width:700px;display:grid;grid-template-columns:1fr 1fr;gap:30px 30px}
.review{display:flex;gap:14px}
.review .photo{flex:0 0 90px;height:90px;background:linear-gradient(135deg,#b88b74,#e9d2c2)}
.review h4{color:var(--blue-text);font-size:15px;font-weight:600}
.stars{display:flex;gap:2px;margin:2px 0}
.review p{font-size:11px;color:var(--muted)}
.review a{font-size:11px}
.contact-form{position:absolute;left:790px;top:0;width:370px;height:330px;border:1px solid var(--line)}
.contact-form h3{background:var(--blue);color:var(--white);font-size:18px;font-weight:600;text-align:center;padding:10px}
.form-body{display:flex;gap:16px;padding:14px}
.field-col{flex:1}
.field-label{font-size:12px;color:var(--ink)}
.field{height:26px;border:1px solid var(--line);margin:2px 0 12px}
.field.message{height:150px}
.contact-form .btn{position:absolute;right:14px;bottom:14px;font-size:12px;padding:5px 16px}

/* footer */
.footer{position:absolute;left:0;top:2420px;width:1200px;height:404px;background:var(--blue);color:var(--white);padding:30px 40px}
.footer-cols{display:flex;gap:40px}
.footer-col{width:250px}
.footer h4{font-size:20px;font-weight:600;margin-bottom:12px}
.footer ul{list-style:none;font-size:13px;line-height:1.6}
.footer a{color:var(--white)}
.contact-line{display:flex;align-items:center;gap:10px;font-size:13px;margin-bottom:12px}
.search-box{height:28px;background:var(--white);border-radius:3px;width:220px;font-size:12px;color:var(--muted);padding:5px 8px}
.footer .btn.light{background:var(--white);color:var(--blue-text);font-size:12px;padding:4px 14px;margin-top:10px}
.socials{display:flex;gap:8px}
.socials span{width:36px;height:36px;border-radius:50%;background:var(--white)}
.footer .map{margin-top:20px;width:260px;height:190px;background:linear-gradient(135deg,#e7e4dc,#cfdcc4 50%,#d6e4f0)}
.book-link{font-size:13px;text-decoration:underline;margin-top:30px;display:block}
.copyright{position:absolute;left:40px;bottom:24px;font-size:12px}
</style>
</head>
<body>
<div class="page">

<header class="hero">
  <div class="photo" role="img" aria-label="Photo of a smiling child at a dental check-up" style="position:absolute;inset:0"></div>
  <div class="brand">
    <span class="brand-mark"></span>
    <div><div class="brand-name">WILLOW DENTAL</div><div class="brand-tag">Family dental care</div></div>
  </div>
  <nav class="main-nav">
    <a class="active">Home</a><a>About us</a><a>Services</a><a>Our Practice</a><a>Smile Gallery</a><a>Blog</a><a>Contact us</a>
  </nav>
  <h1 class="hero-title">Willow Dental</h1>
  <p class="hero-lead">Caring, gentle dentistry for the whole family. Welcome to our blog on healthy, confident and beautiful smiles.</p>
  <a class="btn">More</a>
</header>

<section class="intro">
  <h2>Tooth whitening: what to know</h2>
  <p>Whitening gently lifts stains caused by coffee, tea, wine, smoking and age. At Willow Dental we begin with a check-up, because whitening works best on healthy teeth and gums. Your dentist will explain the choice between in-chair whitening and custom take-home trays, what shade change to expect, and how to manage short-term sensitivity. Crowns, veneers and fillings do not change colour, so we plan around them for an even, natural result.</p>
  <div class="photo" role="img" aria-label="Close-up of a smile before and after tooth whitening"></div>
</section>

<section class="services">
  <div class="service"><div class="photo" role="img" aria-label="Dental implant model" style="background:radial-gradient(#c7d3dc,#7f93a3)"></div><h3>Dental Implants</h3><p>A strong, natural-looking way to replace missing teeth and restore a confident bite.</p><a class="btn">Read More</a></div>
  <div class="service"><div class="photo" role="img" aria-label="Smiling young woman" style="background:radial-gradient(#f1dccd,#b88a70)"></div><h3>Crowns &amp; Veneers</h3><p>Custom-made restorations that repair, protect and reshape worn or chipped teeth.</p><a class="btn">Read More</a></div>
  <div class="service"><div class="photo" role="img" aria-label="Smiling senior woman" style="background:radial-gradient(#eedfd3,#9fb7cc)"></div><h3>R lume Orthodontics</h3><p>Discreet, short-term straightening that gently aligns front teeth for adults.</p><a class="btn">Read More</a></div>
  <div class="service"><div class="photo" role="img" aria-label="Smiling woman with bright teeth" style="background:radial-gradient(#f3e2d6,#c79b83)"></div><h3>Tooth Whitening</h3><p>Safe, dentist-supervised whitening for a brighter smile that still looks like you.</p><a class="btn">Read More</a></div>
</section>

<section class="articles">
  <article class="article"><div class="photo" role="img" aria-label="Family smiling together"></div><div><h3>Why teeth lose their shine</h3><div class="date">2015-05-12</div><p>Stains build up on the surface from coffee, tea, red wine and smoking, while ageing thins enamel so the darker layer beneath shows through. Knowing the cause helps us choose the right whitening.</p></div></article>
  <article class="article"><div class="photo" role="img" aria-label="Diagram of crowns on teeth" style="background:linear-gradient(135deg,#f3f3f3,#d8d8d8 50%,#c27c74)"></div><div><h3>In-chair or take-home?</h3><div class="date">2015-05-19</div><p>In-chair whitening gives a visible change in about an hour. Take-home trays, made to fit your teeth, work gradually over two weeks. Many patients combine both for lasting, even results.</p></div></article>
  <article class="article"><div class="photo" role="img" aria-label="Close-up of a white smile"></div><div><h3>Is whitening safe?</h3><div class="date">2015-05-26</div><p>Professional whitening under a dentist's care is safe for enamel. Some people feel mild sensitivity for a day or two; a desensitising gel and a short break usually settle it quickly.</p></div></article>
  <article class="article"><div class="photo" role="img" aria-label="Teeth with orthodontic braces" style="background:linear-gradient(135deg,#b2514c,#f1e7e0 50%,#9e3f3b)"></div><div><h3>Keeping your smile bright</h3><div class="date">2015-06-02</div><p>Brush twice daily, rinse after dark drinks, use a straw for iced coffee and keep up regular cleans. A quick top-up with your trays every few months keeps results fresh.</p></div></article>
</section>

<section class="testimonials">
  <h2 class="section-title">Testimonials</h2>
  <div class="quotes">
    <div class="quote">I had always hidden my smile in photos. After whitening with my take-home trays my teeth look several shades brighter but still natural. The team explained everything and checked in on me.</div>
    <a class="quote-author">Sarah, whitening patient</a>
    <div class="quote">My crowns and veneers were planned around the whitening so everything matches perfectly. I now smile without thinking about it. Warm, careful and very professional care from start to finish.</div>
    <a class="quote-author">James, veneers patient</a>
  </div>
  <div class="smile-grid">
    <div class="photo" role="img" aria-label="Patient smile after whitening"></div>
    <div class="photo" role="img" aria-label="Patient smile after whitening"></div>
    <div class="photo" role="img" aria-label="Patient smile after whitening"></div>
    <div class="photo" role="img" aria-label="Patient smile after whitening"></div>
    <div class="photo" role="img" aria-label="Patient smile after whitening"></div>
    <div class="photo" role="img" aria-label="Patient smile after whitening"></div>
    <div class="photo" role="img" aria-label="Patient smile after whitening"></div>
    <div class="photo" role="img" aria-label="Patient smile after whitening"></div>
  </div>
</section>

<section class="reviews">
  <h2 class="section-title">Zorvo+ profile reviews</h2>
  <div class="review-list">
    <div class="review"><div class="photo" role="img" aria-label="Reviewer portrait"></div><div><h4>Clara Wendt</h4><div class="stars"><svg width="80" height="14" viewBox="0 0 80 14"><g fill="var(--star)"><polygon points="7,0 9,5 14,5 10,8 11,13 7,10 3,13 4,8 0,5 5,5"/><polygon transform="translate(16 0)" points="7,0 9,5 14,5 10,8 11,13 7,10 3,13 4,8 0,5 5,5"/><polygon transform="translate(32 0)" points="7,0 9,5 14,5 10,8 11,13 7,10 3,13 4,8 0,5 5,5"/><polygon transform="translate(48 0)" points="7,0 9,5 14,5 10,8 11,13 7,10 3,13 4,8 0,5 5,5"/><polygon transform="translate(64 0)" points="7,0 9,5 14,5 10,8 11,13 7,10 3,13 4,8 0,5 5,5"/></g></svg></div><p>Very happy with my whitening results. The team explained each step and made me feel at ease the whole time.</p><a>Read More</a></div></div>
    <div class="review"><div class="photo" role="img" aria-label="Reviewer portrait"></div><div><h4>Priya Osei</h4><div class="stars"><svg width="80" height="14" viewBox="0 0 80 14"><g fill="var(--star)"><polygon points="7,0 9,5 14,5 10,8 11,13 7,10 3,13 4,8 0,5 5,5"/><polygon transform="translate(16 0)" points="7,0 9,5 14,5 10,8 11,13 7,10 3,13 4,8 0,5 5,5"/><polygon transform="translate(32 0)" points="7,0 9,5 14,5 10,8 11,13 7,10 3,13 4,8 0,5 5,5"/><polygon transform="translate(48 0)" points="7,0 9,5 14,5 10,8 11,13 7,10 3,13 4,8 0,5 5,5"/><polygon transform="translate(64 0)" points="7,0 9,5 14,5 10,8 11,13 7,10 3,13 4,8 0,5 5,5"/></g></svg></div><p>Friendly staff and a calm practice. My crown fits perfectly and looks completely natural.</p><a>Read More</a></div></div>
    <div class="review"><div class="photo" role="img" aria-label="Reviewer portrait"></div><div><h4>Hanna L</h4><div class="stars"><svg width="80" height="14" viewBox="0 0 80 14"><g fill="var(--star)"><polygon points="7,0 9,5 14,5 10,8 11,13 7,10 3,13 4,8 0,5 5,5"/><polygon transform="translate(16 0)" points="7,0 9,5 14,5 10,8 11,13 7,10 3,13 4,8 0,5 5,5"/><polygon transform="translate(32 0)" points="7,0 9,5 14,5 10,8 11,13 7,10 3,13 4,8 0,5 5,5"/><polygon transform="translate(48 0)" points="7,0 9,5 14,5 10,8 11,13 7,10 3,13 4,8 0,5 5,5"/><polygon transform="translate(64 0)" points="7,0 9,5 14,5 10,8 11,13 7,10 3,13 4,8 0,5 5,5"/></g></svg></div><p>Gentle care for my kids and clear advice for the whole family. We always leave smiling.</p><a>Read More</a></div></div>
    <div class="review"><div class="photo" role="img" aria-label="Reviewer portrait"></div><div><h4>Rosa Lynn Carver</h4><div class="stars"><svg width="80" height="14" viewBox="0 0 80 14"><g fill="var(--star)"><polygon points="7,0 9,5 14,5 10,8 11,13 7,10 3,13 4,8 0,5 5,5"/><polygon transform="translate(16 0)" points="7,0 9,5 14,5 10,8 11,13 7,10 3,13 4,8 0,5 5,5"/><polygon transform="translate(32 0)" points="7,0 9,5 14,5 10,8 11,13 7,10 3,13 4,8 0,5 5,5"/><polygon transform="translate(48 0)" points="7,0 9,5 14,5 10,8 11,13 7,10 3,13 4,8 0,5 5,5"/><polygon transform="translate(64 0)" points="7,0 9,5 14,5 10,8 11,13 7,10 3,13 4,8 0,5 5,5"/></g></svg></div><p>My veneers changed my confidence. Thorough, honest and caring from the first visit.</p><a>Read More</a></div></div>
  </div>
  <form class="contact-form">
    <h3>Contact Form</h3>
    <div class="form-body">
      <div class="field-col">
        <div class="field-label">Name</div><div class="field"></div>
        <div class="field-label">Email</div><div class="field"></div>
        <div class="field-label">Phone</div><div class="field"></div>
      </div>
      <div class="field-col">
        <div class="field-label">Message</div><div class="field message"></div>
      </div>
    </div>
    <a class="btn">Send</a>
  </form>
</section>

<footer class="footer">
  <div class="footer-cols">
    <div class="footer-col" style="width:200px">
      <h4>Navigation</h4>
      <ul><li>Home</li><li>About Us</li><li>Services</li><li>Our Practice</li><li>Smile Gallery</li><li>Blog</li><li>Contact us</li></ul>
    </div>
    <div class="footer-col" style="width:300px">
      <h4>Contact us</h4>
      <div class="contact-line"><svg width="16" height="20" viewBox="0 0 16 20"><path d="M8 0a7 7 0 0 0-7 7c0 5 7 13 7 13s7-8 7-13a7 7 0 0 0-7-7zm0 10a3 3 0 1 1 0-6 3 3 0 0 1 0 6z" fill="var(--white)"/></svg>12 Fernbrook Lane,<br>Maple Vale VIC 3000</div>
      <div class="contact-line"><svg width="16" height="16" viewBox="0 0 16 16"><path d="M3 0l3 4-2 2c1 2 4 5 6 6l2-2 4 3-2 3C7 16 0 9 0 3z" fill="var(--white)"/></svg>03 5550 0142</div>
      <div class="contact-line"><svg width="18" height="13" viewBox="0 0 18 13"><rect x="0.5" y="0.5" width="17" height="12" fill="none" stroke="var(--white)"/><path d="M1 1l8 6 8-6" fill="none" stroke="var(--white)"/></svg>info@willowdental-example.com.au</div>
      <a class="book-link">Visit www.willowdental-example.com.au</a>
    </div>
    <div class="footer-col">
      <h4>Search</h4>
      <div class="search-box">Type and hit enter</div>
      <a class="btn light">Search</a>
    </div>
    <div class="footer-col" style="width:260px">
      <h4>Social Media</h4>
      <div class="socials"><span></span><span></span><span></span><span></span></div>
      <div class="map" role="img" aria-label="Street map showing the practice location"></div>
    </div>
  </div>
  <p class="copyright">Copyright 2015 &copy; Willow Dental Practice. All rights reserved.</p>
</footer>

</div>
</body>
</html>
```